Packaging design for a revolutionary hi-protein snack of Norwegian salmon

We need a breathtaking packing design for a smal snack bag (30 g) for a revolutionary new hi-protein snack made of Norwegian salmon. The product will be made with two different flavors; MANGO and WASABI. The product is extreme high in protein (60%) and omega 3, and are just natural.

We want to see a bold and fresh design that appeals to protein lovers of all ages.

Target Market(s)

Our target market is boys and girls that are 18-35 years old and that are interested in working out and eating healthy.

Industry/Entity Type

Snack industry (functional food, healthy snack, protein snack)

Font styles to use
Sans Serif

Requirements
Must have
• The package design must give the customer a WOW feeling. "HI-PROTEIN SNACK" must be highligted. Further, the design must use the Four Factors setup (attached).

```html
<!DOCTYPE html>
<html lang="en">
<head>
<meta charset="utf-8">
<title>Tidal Bite Hi-Protein Snack Packs</title>
<link href="https://fonts.googleapis.com/css2?family=Montserrat:wght@500;600;800&family=Great+Vibes&display=swap" rel="stylesheet">
<style>
  :root {
    --stage: #a9a9a9;
    --cream: #fdf5cf;
    --ink: #121212;
    --white: #ffffff;
  }
  .pack--wasabi {
    --main: #6aa80f;
    --light: #a2d22a;
    --deep: #3f7a0a;
    --accent: #5b9a12;
    --tag: #3f7a0a;
  }
  .pack--mango {
    --main: #f0c20a;
    --light: #ffdc45;
    --deep: #e08f14;
    --accent: #ec7a16;
    --tag: #ec7a16;
  }
  html, body {
    margin: 0;
    padding: 0;
    width: 1200px;
    height: 1200px;
    overflow: hidden;
    background: var(--stage);
    font-family: "Montserrat", Arial, sans-serif;
  }
  .stage {
    position: relative;
    width: 1200px;
    height: 1200px;
  }
  .pack {
    position: absolute;
    top: 270px;
    width: 440px;
    height: 620px;
  }
  .pack--wasabi { left: 110px; }
  .pack--mango { left: 650px; }
  .pack__shape {
    position: absolute;
    inset: 0;
    width: 440px;
    height: 620px;
  }
  .shape-main { fill: var(--main); }
  .shape-light { fill: var(--light); }
  .shape-cream { fill: var(--cream); }
  .shape-stage { fill: var(--stage); }
  .brand {
    position: absolute;
    top: 108px;
    left: 0;
    width: 240px;
    text-align: center;
    font-weight: 800;
    font-size: 30px;
    line-height: 0.95;
    color: var(--main);
    letter-spacing: -0.5px;
  }
  .headline {
    position: absolute;
    top: 196px;
    left: 0;
    width: 440px;
    text-align: center;
  }
  .headline__main {
    display: block;
    font-weight: 800;
    font-size: 54px;
    line-height: 1;
    color: var(--ink);
    letter-spacing: -0.5px;
  }
  .headline__script {
    display: block;
    margin-top: -18px;
    font-family: "Great Vibes", cursive;
    font-size: 92px;
    line-height: 1;
    color: var(--accent);
  }
  .product-photo {
    position: absolute;
    top: 330px;
    left: 120px;
    width: 210px;
    height: 200px;
    border-radius: 48% 52% 40% 60% / 55% 45% 55% 45%;
    background: radial-gradient(circle at 45% 40%, #f5a466, #e0622b 70%, #c44a1f);
  }
  .badge {
    position: absolute;
    top: 468px;
    right: 24px;
    display: flex;
    align-items: center;
    gap: 6px;
  }
  .badge__icon {
    width: 52px;
    height: 26px;
    border-radius: 50%;
    background: #e8e8e8;
  }
  .badge__text {
    font-weight: 800;
    font-size: 13px;
    line-height: 1.05;
    color: var(--white);
  }
  .badge__text span {
    display: block;
    font-weight: 600;
    color: var(--tag);
  }
  .info {
    position: absolute;
    top: 520px;
    left: 24px;
    right: 24px;
  }
  .info__row {
    display: flex;
    justify-content: space-between;
    align-items: flex-end;
  }
  .flavor {
    background: var(--tag);
    color: var(--white);
    font-weight: 500;
    font-size: 20px;
    padding: 4px 10px;
    letter-spacing: 0.5px;
  }
  .weight {
    background: var(--tag);
    color: var(--white);
    font-weight: 500;
    font-size: 28px;
    padding: 2px 18px;
    margin-bottom: 6px;
  }
  .claim {
    background: rgba(255, 255, 255, 0.22);
    color: var(--white);
    font-weight: 500;
    font-size: 15px;
    line-height: 1.1;
    padding: 6px 12px;
    width: 320px;
  }
</style>
</head>
<body>
<main class="stage">

  <section class="pack pack--wasabi">
    <svg class="pack__shape" viewBox="0 0 440 620" aria-hidden="true">
      <rect class="shape-main" x="0" y="0" width="440" height="620"/>
      <path class="shape-light" d="M0 40 H440 V80 Q400 60 360 78 T280 78 T200 80 T120 76 T40 80 L0 74 Z"/>
      <path class="shape-cream" d="M0 92 Q40 70 80 88 T160 88 T240 86 T320 90 T400 84 L440 90 V420 Q400 400 360 416 T280 440 T200 452 T120 442 T40 430 L0 436 Z"/>
      <path class="shape-light" d="M0 436 Q40 430 120 442 T280 440 T440 420 V450 Q360 470 280 462 T120 470 T0 480 Z"/>
      <rect class="shape-main" x="0" y="590" width="440" height="30"/>
      <path class="shape-stage" d="M212 44 h16 v8 l-8 6 l-8 -6 Z"/>
    </svg>
    <div class="brand">tidal<br>bite</div>
    <h1 class="headline">
      <span class="headline__main">HI-PROTEIN</span>
      <span class="headline__script">Snack</span>
    </h1>
    <div class="product-photo" role="img" aria-label="Photo of dried salmon snack pieces"></div>
    <div class="badge">
      <div class="badge__icon" role="img" aria-label="Small fish illustration"></div>
      <div class="badge__text"><span>100%</span>NATURAL</div>
    </div>
    <div class="info">
      <div class="info__row">
        <div class="flavor">WASABI</div>
        <div class="weight">30 g</div>
      </div>
      <div class="claim">HIGH IN PROTEIN (60%) AND OMEGA 3</div>
    </div>
  </section>

  <section class="pack pack--mango">
    <svg class="pack__shape" viewBox="0 0 440 620" aria-hidden="true">
      <rect class="shape-main" x="0" y="0" width="440" height="620"/>
      <path class="shape-light" d="M0 40 H440 V80 Q400 60 360 78 T280 78 T200 80 T120 76 T40 80 L0 74 Z"/>
      <path class="shape-cream" d="M0 92 Q40 70 80 88 T160 88 T240 86 T320 90 T400 84 L440 90 V420 Q400 400 360 416 T280 440 T200 452 T120 442 T40 430 L0 436 Z"/>
      <path class="shape-light" d="M0 436 Q40 430 120 442 T280 440 T440 420 V450 Q360 470 280 462 T120 470 T0 480 Z"/>
      <rect class="shape-main" x="0" y="590" width="440" height="30"/>
      <path class="shape-stage" d="M212 44 h16 v8 l-8 6 l-8 -6 Z"/>
    </svg>
    <div class="brand">tidal<br>bite</div>
    <h1 class="headline">
      <span class="headline__main">HI-PROTEIN</span>
      <span class="headline__script">Snack</span>
    </h1>
    <div class="product-photo" role="img" aria-label="Photo of dried salmon snack pieces"></div>
    <div class="badge">
      <div class="badge__icon" role="img" aria-label="Small fish illustration"></div>
      <div class="badge__text"><span>100%</span>NATURAL</div>
    </div>
    <div class="info">
      <div class="info__row">
        <div class="flavor">MANGO</div>
        <div class="weight">30 g</div>
      </div>
      <div class="claim">HIGH IN PROTEIN (60%) AND OMEGA 3</div>
    </div>
  </section>

</main>
</body>
</html>
```